Home Page Website Design

The Site width is 1000 px. I've attached a Balsamiq mockup as a design layout guide. The design needs to be flat and clean. Please stick to the pixel dimensions of the mock up as the site will be responsive. I've also attached the logos used on the mockup for positional purposes.

Colours to use: Black, Grey, Green (Logo tie in) & green complementary colours.

Green (Logo tie in)
White Background
Titles: Black (Roboto Bold 700)
Text: Dark Grey (Roboto Normal 400)

Look & Style Example
http://www.brindlowlearn.org.uk/

Type Face
Google Fonts - Roboto

These are just guidelines, please feel free to use you own creative judgment.

Thanks

```html
<!DOCTYPE html>
<html lang="en">
<head>
<meta charset="utf-8">
<title>Brindlow Teaching School Alliance – Home</title>
<link href="https://fonts.googleapis.com/css2?family=Roboto:wght@400;500;700&display=swap" rel="stylesheet">
<style>
:root{
  --green:#00a94f;
  --black:#000;
  --ink:#111;
  --text:#555;
  --heading:#333;
  --grey:#d9d9d9;
  --grey-mid:#c8c8c8;
  --grey-light:#e6e6e6;
  --white:#fff;
  --footer:#0c0c0c;
  --footer-mid:#1e1e1e;
  --tab:#666;
}
*{box-sizing:border-box;margin:0;padding:0}
html,body{width:819px;height:1200px;overflow:hidden;background:var(--white)}
body{font-family:'Roboto',Arial,sans-serif;color:var(--text)}
.site{width:1000px;height:1465px;transform:scale(.819);transform-origin:0 0;position:relative;background:var(--white);overflow:hidden}

/* header */
.masthead{height:113px;background:var(--black);position:relative}
.brand{position:absolute;left:15px;top:18px;display:flex;align-items:center;gap:16px}
.brand-mark{width:18px;height:18px;background:var(--green)}
.brand-name{color:var(--white);font-weight:700;font-size:21px;line-height:20px;width:110px}
.utility{position:absolute;right:18px;top:18px;color:var(--white);font-weight:500;font-size:14px;display:flex;align-items:center;gap:14px}
.chat-dot{width:26px;height:16px;border-radius:50%;background:var(--green)}
.search{position:absolute;right:15px;top:56px;width:245px;height:26px;background:var(--white);border:1px solid #bbb;font-size:12px;color:#999;padding:6px 8px}

/* nav */
.nav{height:57px;display:flex;border-bottom:1px solid #ddd}
.nav a{color:var(--ink);text-decoration:none;font-size:14px;padding:0 10px;line-height:57px;border-right:1px solid #ddd;white-space:nowrap}
.nav a:first-child{padding-left:13px}
.nav a:last-child{border:none}
.register{position:absolute;left:757px;top:103px;width:212px;height:78px;background:var(--green);padding:10px 12px}
.register h3{color:var(--white);font-size:21px;font-weight:700;text-align:center;white-space:nowrap}
.register .field{display:flex;align-items:center;margin-top:6px;gap:8px}
.register .input{width:160px;height:22px;background:var(--white);font-size:11px;color:#999;padding:4px 6px}

/* hero */
.hero{height:330px;display:flex}
.hero-copy{width:400px;background:var(--grey);padding:20px 20px;position:relative}
.hero-copy h1{color:var(--ink);font-size:28px;font-weight:700;margin-bottom:10px;white-space:nowrap}
.hero-copy p{font-size:14px;line-height:20px;color:var(--text)}
.btn{display:inline-block;background:var(--green);color:var(--white);font-weight:500;font-size:13px;border-radius:3px;padding:8px 12px;text-decoration:none;white-space:nowrap}
.hero-copy .btn{position:absolute;right:-10px;top:270px;height:32px;line-height:32px;padding:0 11px}
.hero-photo{flex:1;background:linear-gradient(120deg,#3a2c22 0%,#7a6552 40%,#b7a78f 60%,#4b3a2e 100%)}

/* columns */
.columns{display:flex;gap:20px;padding:20px 15px;height:593px}
.panel{width:310px;height:553px;border:1px solid #ccc;border-top:none}
.panel-title{background:var(--green);color:var(--white);font-size:26px;font-weight:700;height:58px;padding:18px 14px 0;white-space:nowrap}
.panel p{font-size:13px;line-height:20px;color:var(--text)}
.welcome .player{margin:17px 14px 14px;height:198px;border:1px solid #aaa;background:linear-gradient(#fff,#eee);position:relative}
.player .play{position:absolute;left:110px;top:60px;width:58px;height:48px;border-radius:8px;background:linear-gradient(#ddd,#999);box-shadow:0 3px 6px rgba(0,0,0,.4)}
.player .bar{position:absolute;left:0;right:0;bottom:0;height:22px;background:linear-gradient(#eee,#bbb);border-top:1px solid #999;font-size:10px;color:#222;padding:4px 58px}
.welcome p{padding:0 14px}
.col-mid{display:flex;flex-direction:column;gap:34px;width:310px;height:553px}
.col-mid .panel{height:auto}
.training{border:none}
.training-list{list-style:none}
.training-list li{height:38px;padding:0 14px;font-size:16px;font-weight:500;color:var(--heading);display:flex;justify-content:space-between;align-items:center}
.training-list li:nth-child(odd){background:var(--grey-mid)}
.training-list li:nth-child(even){background:var(--grey-light)}
.news{flex:1}
.news article{padding:12px 14px 8px}
.news h4,.course h4{font-size:16px;line-height:20px;font-weight:500;color:var(--heading);margin-bottom:1px}
.course{height:168px;padding:12px 14px 0}
.course p{margin-bottom:8px}
.course .btn{position:relative;left:-25px;border-radius:0 3px 3px 0;font-size:12px;height:31px;line-height:31px;padding:0 25px}
.course .btn::before{content:"";position:absolute;left:0;top:-12px;width:8px;height:12px;background:var(--tab);border-radius:4px 0 0 0}

/* footer */
.footer{height:221px;background:var(--footer);display:flex;color:var(--white);font-size:12px}
.footer-col{padding:26px 20px;border-right:2px solid #333;background:linear-gradient(#111,var(--footer-mid))}
.footer-about{width:276px;background:var(--footer);line-height:15px;padding:26px 25px}
.footer-about .brand-name{font-size:18px;line-height:20px;width:auto;margin-bottom:10px}
.footer-about .copy{color:#aaa;margin-top:14px}
.footer-col h5{font-size:13px;font-weight:500;margin-bottom:12px}
.footer-col ul{list-style:none}
.footer-col li{margin-bottom:12px;display:flex;align-items:center;gap:7px;line-height:14px}
.footer-links{width:242px}
.icon{width:14px;height:14px;border-radius:2px}
.network{flex:1;border:none;display:flex;align-items:center;justify-content:center;gap:12px}
.network .name{font-size:20px;line-height:21px;font-weight:400;width:90px}
.network .dot{width:22px;height:22px;border-radius:50%;background:#b9d531}

/* partners */
.partners{text-align:center;padding-top:14px;height:151px}
.partners h6{font-size:11px;font-weight:400;color:var(--heading);letter-spacing:.5px;margin-bottom:10px}
.partner-row{display:flex;justify-content:space-between;align-items:center;padding:0 14px}
.badge{background:#cfd4dc}
</style>
</head>
<body>
<div class="site">

  <header class="masthead">
    <div class="brand"><span class="brand-mark"></span><span class="brand-name">Brindlow Teaching School Alliance</span></div>
    <div class="utility"><span>Live Chat</span><span class="chat-dot"></span><span>|</span><span>Login</span></div>
    <div class="search">Search...</div>
  </header>

  <nav class="nav">
    <a href="#">Home</a><a href="#">About Us</a><a href="#">Training &amp; Development</a><a href="#">Benefits</a><a href="#">Members</a><a href="#">What’s On</a><a href="#">Contact Us</a><a href="#">News</a><a href="#">Forum</a>
  </nav>

  <div class="register">
    <h3>REGISTER NOW!</h3>
    <div class="field"><div class="input">Email address</div>
      <svg width="26" height="20" viewBox="0 0 26 20"><path d="M2 2l10 8-10 8zM13 2l10 8-10 8z" fill="#fff"/></svg></div>
  </div>

  <section class="hero">
    <div class="hero-copy">
      <h1>New Teachers in Workshop</h1>
      <p>Sed ut perspiciatis, unde omnis iste natus error sit voluptatem accusantium doloremque laudantium, totam rem aperiam eaque ipsa, quae ab illo inventore veritatis et quasi architecto beatae vitae dicta sunt, explicabo. Nemo enim ipsam voluptatem, quia voluptas sit, aspernatur aut odit aut fugit, sed quia consequuntur magni dolores eos, qui ratione voluptatem sequi nesciunt, neque porro quisquam est, qui dolorem ipsum, quia dolor sit amet, consectetur, adipisci[ng] velit, sed quia non numquam [do] eius modi tempora inci[di]dunt, ut labore et dolore.</p>
      <a class="btn" href="#">Find Out More...</a>
    </div>
    <div class="hero-photo" role="img" aria-label="Photo of an experienced teacher leading a discussion with new teachers around a table"></div>
  </section>

  <main class="columns">
    <section class="panel welcome">
      <div class="panel-title">Welcome</div>
      <div class="player">
        <div class="play"><svg width="58" height="48" viewBox="0 0 58 48"><path d="M22 14l16 10-16 10z" fill="#222"/></svg></div>
        <div class="bar">0:00 / 1:00</div>
        <svg style="position:absolute;left:6px;bottom:4px" width="44" height="14" viewBox="0 0 44 14"><path d="M2 1l10 6-10 6z" fill="#222"/><path d="M24 5h3l4-3v10l-4-3h-3z" fill="#333"/></svg>
      </div>
      <p>Sed ut perspiciatis, unde omnis iste natus error sit voluptatem accusantium doloremque laudantium, totam rem aperiam eaque ipsa, quae ab illo inventore veritatis et quasi architecto beatae vitae dicta sunt, explicabo. Nemo enim ipsam voluptatem, quia voluptas sit, aspernatur aut odit aut fugit, sed quia consequuntur magni dolores eos, qui ratione voluptatem sequi nesciunt, neque porro quisquam est, qui dolorem ipsum, quia dolor sit amet, consectetur, adipisci[ng] velit, sed quia non numquam [do] eius modi tempora inci[di]dunt, ut labore et dolore.</p>
    </section>

    <div class="col-mid">
      <section class="panel training">
        <div class="panel-title">Training &amp; Development</div>
        <ul class="training-list">
          <li>Leadership Training<svg width="22" height="22" viewBox="0 0 22 22"><path d="M2 1l19 10-19 10 5-10z" fill="#555"/></svg></li>
          <li>CPD<svg width="22" height="22" viewBox="0 0 22 22"><path d="M2 1l19 10-19 10 5-10z" fill="#555"/></svg></li>
          <li>School 2 School Support<svg width="22" height="22" viewBox="0 0 22 22"><path d="M2 1l19 10-19 10 5-10z" fill="#555"/></svg></li>
          <li>Research &amp; Development<svg width="22" height="22" viewBox="0 0 22 22"><path d="M2 1l19 10-19 10 5-10z" fill="#555"/></svg></li>
          <li>ITT (School Direct)<svg width="22" height="22" viewBox="0 0 22 22"><path d="M2 1l19 10-19 10 5-10z" fill="#555"/></svg></li>
        </ul>
      </section>
      <section class="panel news">
        <div class="panel-title">News</div>
        <article><h4>Lorem ipum dolor sit amet</h4><p>Sed ut perspiciatis, unde omnis iste natus error sit voluptatem accusantium doloremque.</p></article>
        <article><h4>Lorem ipum dolor sit amet</h4><p>Sed ut perspiciatis, unde omnis iste natus error sit voluptatem accusantium doloremque. Sed ut perspiciatis, unde omnis iste natus error sit voluptatem accusantium doloremque.</p></article>
      </section>
    </div>

    <section class="panel courses">
      <div class="panel-title">Latest Courses</div>
      <div class="course"><h4>Want to deliver consistency ‘Outstanding’ Lessons?</h4><p>Sed ut perspiciatis, unde omnis iste natus error sit voluptatem accusantium doloremque.</p><a class="btn" href="#">6 places left: Book now &gt;</a></div>
      <div class="course"><h4>School Direct Initial Teacher Training- Places still available</h4><p>Sed ut perspiciatis, unde omnis iste natus error sit voluptatem accusantium doloremque.</p><a class="btn" href="#">2 places left: Book now &gt;</a></div>
      <div class="course"><h4>Take a look at our Newly Qualified Teacher Learning Packages!</h4><p>Sed ut perspiciatis, unde omnis iste natus error sit voluptatem accusantium doloremque. Sed ut perspiciatis, unde omnis iste natus error sit.</p><a class="btn" href="#">10 places left: Book now &gt;</a></div>
    </section>
  </main>

  <footer class="footer">
    <div class="footer-col footer-about">
      <div class="brand-name">Brindlow</div>
      <strong>Brindlow Teaching Schools Alliance</strong><br>Ashford Lane<br>Brindlow<br>BR4 7QL<br>Tel: 01632 960418<br>hello@brindlowlearn.org.uk
      <div class="copy">© 2013 Brindlow Teaching Schools Alliance</div>
    </div>
    <div class="footer-col footer-links">
      <h5>LEARN MORE</h5>
      <ul><li>About Us</li><li>Training &amp; Development</li><li>Benefits</li><li>News</li><li>Members</li><li>Calendar of Events</li></ul>
    </div>
    <div class="footer-col footer-links">
      <h5>CONNECT</h5>
      <ul>
        <li><span class="icon" style="background:#f6d66b"></span>Contact Us</li>
        <li><span class="icon" style="background:#e85a3c"></span>Forum</li>
        <li><span class="icon" style="background:#4aa9e0"></span>Chirper</li>
        <li><span class="icon" style="background:#3b5ea8"></span>FriendBook</li>
        <li style="margin-top:26px">Site Map</li>
      </ul>
    </div>
    <div class="footer-col network"><span class="dot"></span><span class="name">National Learning Network</span></div>
  </footer>

  <section class="partners">
    <h6>PARTNER SCHOOLS</h6>
    <div class="partner-row">
      <div class="badge" style="width:66px;height:84px;border-radius:6px"></div>
      <div class="badge" style="width:52px;height:84px;background:#3a8a4a"></div>
      <div class="badge" style="width:58px;height:84px;border-radius:50% 50% 6px 6px"></div>
      <div class="badge" style="width:68px;height:72px;background:#1b2f8f"></div>
      <div class="badge" style="width:62px;height:72px;border-radius:50%;background:#2a4b9b"></div>
      <div class="badge" style="width:66px;height:72px;background:#2a4b9b;border-radius:8px"></div>
      <div class="badge" style="width:42px;height:88px;background:#b9333b"></div>
      <div class="badge" style="width:102px;height:34px;background:#1d74bf"></div>
      <div class="badge" style="width:118px;height:46px;background:#c8102e;border-radius:4px"></div>
      <div class="badge" style="width:68px;height:78px;background:#1b2f6b;border-radius:50%"></div>
      <div class="badge" style="width:120px;height:70px;background:#e2e6f0"></div>
    </div>
  </section>

</div>
</body>
</html>
```